Organic Coconut oil

A label for a 500ml jar of organic coconut oil
The product is raw cold pressed virgin coconut oil
Target Market(s)
All health conscious individuals
Industry/Entity Type
Product
Requirements
Must have
- Virgin
Raw
Cold pressed
Organic
Product name tibu coconut oil

```html
<!DOCTYPE html>
<html lang="en">
<head>
<meta charset="utf-8">
<title>Tibu Coconut Oil – Jar Label</title>
<link rel="stylesheet" href="https://fonts.googleapis.com/css2?family=Bebas+Neue&family=Playfair+Display:ital,wght@1,700&display=swap">
<style>
  :root {
    --page-bg: #ffffff;
    --leaf-green: #3f8a2e;
    --leaf-light: #68ad48;
    --husk-brown: #80522a;
    --flesh-cream: #e9e3d6;
    --tag-brown: #8b5a2b;
    --band-brown: #5b3322;
    --brand-brown: #5a2c1c;
    --text-light: #ffffff;
  }
  html, body {
    margin: 0;
    width: 1200px;
    height: 848px;
    overflow: hidden;
    background: var(--page-bg);
  }
  .label {
    position: absolute;
    left: 538px;
    top: 218px;
    width: 446px;
    height: 334px;
    overflow: hidden;
    box-shadow: 4px 6px 8px rgba(0,0,0,0.35);
  }
  .label-photo {
    position: absolute;
    inset: 0;
    background: linear-gradient(100deg,
      var(--husk-brown) 0%,
      var(--flesh-cream) 32%,
      var(--husk-brown) 56%,
      var(--leaf-green) 72%,
      var(--leaf-light) 100%);
  }
  .brand-name {
    position: absolute;
    left: 108px;
    top: 10px;
    margin: 0;
    font-family: "Bebas Neue", sans-serif;
    font-weight: 400;
    font-size: 46px;
    line-height: 0.9;
    color: var(--brand-brown);
    transform: rotate(-7deg);
    transform-origin: left bottom;
  }
  .brand-name__first {
    display: block;
    padding-left: 52px;
  }
  .brand-name__rest { display: block; }
  .claims {
    list-style: none;
    margin: 0;
    padding: 0;
  }
  .claim {
    position: absolute;
    right: 1px;
    height: 37px;
    padding: 0 6px;
    background: var(--tag-brown);
    color: var(--text-light);
    font-family: "Bebas Neue", sans-serif;
    font-size: 37px;
    line-height: 40px;
    letter-spacing: 0.3px;
  }
  .claim--raw { top: 53px; }
  .claim--cold { top: 111px; }
  .claim--virgin { top: 169px; }
  .claim--oil { top: 227px; }
  .volume-band {
    position: absolute;
    left: 0;
    right: 0;
    top: 302px;
    height: 22px;
    background: var(--band-brown);
  }
  .volume, .organic {
    position: absolute;
    top: 1px;
    font-family: "Playfair Display", serif;
    font-style: italic;
    font-weight: 700;
    font-size: 16px;
    line-height: 20px;
    font-variant-numeric: lining-nums;
    color: var(--text-light);
  }
  .volume { left: 8px; }
  .organic { right: 8px; }
</style>
</head>
<body>
  <section class="label">
    <div class="label-photo" role="img" aria-label="Photo of a halved coconut with white flesh on green palm leaves"></div>
    <h1 class="brand-name"><span class="brand-name__first">Tibu</span><span class="brand-name__rest">Coconut Oil</span></h1>
    <ul class="claims">
      <li class="claim claim--raw">Raw</li>
      <li class="claim claim--cold">Cold Pressed</li>
      <li class="claim claim--virgin">Virgin</li>
      <li class="claim claim--oil">Coconut Oil</li>
    </ul>
    <div class="volume-band"><span class="volume">500ml</span><span class="organic">Organic</span></div>
  </section>
</body>
</html>
```